Tavrelo LLC banner ad design project

I want banner advertisements designed in various ad formats-the most popular sizes according to Plinkora Spots (600x450, 300x250, 250x250, 120x600).
Please put in the ads a picture of the bottle (attached) and a picture of a slim woman/man (preferably woman, as I am targetting a largely female audience) in the advertisement.
As for the text of the ads, I'd like for there to be something like the following:
"Lose 15 lbs in 3 months"
"Lose weight with traditional Chinese medicine"
"Lose weight using ancient Chinese herbs"
Also please feel free to use other text using some of the articles on my site, which can be found at the following link:
http://www.tavrelo-example.com/
Thanks, and if you have any additional questions, please don't hesitate to ask.
Additional notes: would also like for you to follow the color scheme on my website (orange, green) for the most part, although please when submitting different ads make sure to include other color schemes, as some of those color schemes may work better for the ads than the green/orange color scheme.
I've also attached an ad from Vembrashed that should give you an idea of something similar I'm looking for (though please submit multiple ideas)!
Updates
Industry/Entity Type
Weight
Look and feel
Each slider illustrates characteristics of the customer's brand and the style your logo design should communicate.

```html
<!DOCTYPE html>
<html lang="en">
<head>
<meta charset="utf-8">
<title>Tavrelo banner set</title>
<link rel="stylesheet" href="https://fonts.googleapis.com/css2?family=Dosis:wght@500;600&family=Ubuntu:wght@400;500&display=swap">
<style>
  :root {
    --stage: #40474a;
    --green: #1a8f3c;
    --green-dark: #0f7a30;
    --orange: #f0641e;
    --orange-dark: #d84f10;
    --brand-orange: #d9561c;
    --grey-text: #7a6f6a;
    --paper: #ffffff;
    --mist-1: #f4f4f4;
    --mist-2: #dcdcdc;
  }
  * { box-sizing: border-box; margin: 0; padding: 0; }
  html, body { width: 1200px; height: 750px; overflow: hidden; }
  body { background: var(--stage); position: relative; font-family: "Ubuntu", Arial, sans-serif; }

  .banner { position: absolute; background: var(--paper); overflow: hidden; }
  .banner > * { position: absolute; }
  .backdrop { inset: 0; background: linear-gradient(180deg, var(--mist-1) 0%, var(--mist-2) 70%, #eeeeee 100%); }
  .bottle-photo { background: linear-gradient(90deg, #e9ecea 0%, #ffffff 45%, #d7dbd8 100%); border-radius: 18px 18px 10px 10px; }
  .model-photo { background: linear-gradient(180deg, #f1d6c6 0%, #ef7a3a 35%, #ee6e2c 55%, #e8c3ae 75%, #f0d8ca 100%); border-radius: 40px 40px 10px 10px; opacity: .92; }
  .model-photo.green-top { background: linear-gradient(180deg, #f1d6c6 0%, #2e9a45 45%, #35a04c 100%); }
  .swoosh { inset: 0; width: 100%; height: 100%; }

  .headline { font-family: "Dosis", Arial, sans-serif; font-weight: 600; color: var(--green); line-height: 1; }
  .subline { color: var(--grey-text); line-height: 1.3; }
  .accent-line { font-family: "Dosis", Arial, sans-serif; font-weight: 600; color: var(--orange); letter-spacing: 3px; }

  .cta { display: flex; align-items: center; justify-content: center; text-align: center;
         color: #fff; font-weight: 500; line-height: 1.25;
         background: linear-gradient(180deg, #f88a45 0%, var(--orange) 45%, var(--orange-dark) 100%);
         border: 2px solid #ffb07a; box-shadow: 0 2px 3px rgba(0,0,0,.25); }
  .cta.pill { border-radius: 26px; }
  .cta.block { border-radius: 4px; }

  .brand-name { font-family: "Ubuntu", Arial, sans-serif; font-weight: 500; color: var(--brand-orange); line-height: 1; display: flex; align-items: center; gap: 6px; }
  .brand-dot { display: inline-block; border-radius: 50%; background: var(--green); }

  .natural-badge { border-radius: 50%; background: var(--green); border: 3px solid #fff; color: #fff;
                   display: flex; flex-direction: column; align-items: center; justify-content: center;
                   font-family: Georgia, serif; font-style: italic; font-weight: 700; line-height: .95; }
  .natural-badge.orange { background: var(--orange); }
  .natural-badge .pct { font-size: 1.6em; }
  .natural-badge .pct sup { font-size: .45em; }

  .benefits { list-style: none; color: var(--grey-text); font-size: 16px; font-weight: 500; }
  .benefits li { margin-bottom: 8px; }
  .benefits li::before { content: "•"; color: #999; margin-right: 9px; font-size: 12px; }
  .benefits strong { color: var(--green); font-weight: 500; }
</style>
</head>
<body>

<!-- 600 x 450 -->
<section class="banner banner-large" style="left:53px;top:127px;width:599px;height:448px;">
  <div class="backdrop" role="img" aria-label="Misty traditional temple scenery backdrop"></div>
  <svg class="swoosh" viewBox="0 0 599 448" preserveAspectRatio="none" aria-hidden="true">
    <path d="M0 438 C220 430 420 390 599 336 L599 448 L0 448 Z" fill="var(--paper)"/>
    <path d="M120 432 C300 420 450 385 599 336" fill="none" stroke="var(--green)" stroke-width="7"/>
  </svg>
  <div class="bottle-photo" role="img" aria-label="Supplement bottle with herbal label" style="left:12px;top:100px;width:200px;height:340px;"></div>
  <div class="model-photo" role="img" aria-label="Slim woman in orange sportswear stretching arms up" style="left:152px;top:0;width:140px;height:448px;"></div>
  <h1 class="headline" style="left:282px;top:46px;width:305px;text-align:center;font-size:48px;">LOSE 15 LBS</h1>
  <div style="left:282px;top:96px;width:305px;height:1px;background:#aaa;"></div>
  <p class="accent-line" style="left:282px;top:102px;width:305px;text-align:center;font-size:25px;">IN 3 MONTHS</p>
  <p class="subline" style="left:282px;top:138px;width:305px;text-align:center;font-size:18px;">with Traditional Chinese Medicine</p>
  <ul class="benefits" style="left:298px;top:180px;">
    <li>Clinically proven weight loss tool</li>
    <li><strong>TARGETS</strong> excess belly fat</li>
    <li><strong>INCREASES</strong> metabolism</li>
  </ul>
  <div class="cta pill" style="left:297px;top:273px;width:216px;height:46px;font-size:16px;">TRY TAVRELO TODAY</div>
  <div class="brand-name" style="left:430px;top:392px;font-size:32px;"><span class="brand-dot" style="width:12px;height:12px;"></span>TAVRELO</div>
  <div class="natural-badge" style="left:140px;top:340px;width:92px;height:92px;font-size:17px;"><span class="pct">100<sup>%</sup></span><span>natural</span></div>
</section>

<!-- 250 x 250 -->
<section class="banner banner-square" style="left:687px;top:52px;width:249px;height:249px;">
  <div class="backdrop" role="img" aria-label="Soft misty backdrop"></div>
  <svg class="swoosh" viewBox="0 0 249 249" preserveAspectRatio="none" aria-hidden="true">
    <path d="M0 150 C80 170 150 190 249 214 L249 249 L0 249 Z" fill="var(--paper)"/>
    <path d="M0 150 C80 170 150 190 249 214" fill="none" stroke="var(--orange)" stroke-width="6"/>
  </svg>
  <div class="bottle-photo" role="img" aria-label="Supplement bottle" style="left:172px;top:14px;width:77px;height:186px;"></div>
  <div class="model-photo green-top" role="img" aria-label="Slim woman in green sportswear posing" style="left:133px;top:44px;width:60px;height:205px;"></div>
  <h2 class="headline" style="left:15px;top:14px;font-size:25px;">Lose weight</h2>
  <p class="subline" style="left:17px;top:46px;font-size:14px;">using ancient<br>Chinese herbs</p>
  <div class="cta pill" style="left:10px;top:97px;width:148px;height:42px;font-size:13px;">TRY TAVRELO TODAY</div>
  <div class="brand-name" style="left:10px;top:204px;font-size:25px;">TAVRELO</div>
  <div class="natural-badge" style="left:182px;top:180px;width:58px;height:58px;font-size:12px;"><span class="pct">100<sup>%</sup></span><span>natural</span></div>
</section>

<!-- 300 x 250 -->
<section class="banner banner-rectangle" style="left:686px;top:326px;width:299px;height:249px;">
  <div class="backdrop" role="img" aria-label="Soft misty backdrop"></div>
  <svg class="swoosh" viewBox="0 0 299 249" preserveAspectRatio="none" aria-hidden="true">
    <path d="M0 170 C90 175 180 200 299 225 L299 249 L0 249 Z" fill="var(--paper)"/>
    <path d="M0 170 C90 175 180 200 299 225" fill="none" stroke="var(--green)" stroke-width="6"/>
  </svg>
  <div class="bottle-photo" role="img" aria-label="Supplement bottle" style="left:200px;top:42px;width:99px;height:207px;"></div>
  <div class="model-photo" role="img" aria-label="Slim woman in orange sportswear stretching" style="left:150px;top:0;width:72px;height:249px;"></div>
  <h2 class="headline" style="left:14px;top:13px;font-size:25px;">Lose weight</h2>
  <p class="subline" style="left:16px;top:45px;font-size:14px;">with Traditional<br>Chinese Medicine</p>
  <div class="cta pill" style="left:12px;top:97px;width:142px;height:42px;font-size:13px;">TRY TAVRELO TODAY</div>
  <div class="brand-name" style="left:10px;top:202px;font-size:25px;">TAVRELO</div>
  <div class="natural-badge" style="left:186px;top:168px;width:58px;height:58px;font-size:12px;"><span class="pct">100<sup>%</sup></span><span>natural</span></div>
</section>

<!-- 120 x 600 -->
<section class="banner banner-skyscraper" style="left:1028px;top:52px;width:119px;height:599px;">
  <div class="backdrop" role="img" aria-label="Soft misty backdrop" style="top:90px;"></div>
  <svg class="swoosh" viewBox="0 0 119 599" preserveAspectRatio="none" aria-hidden="true">
    <path d="M0 0 L119 0 L119 70 C80 80 40 92 0 100 Z" fill="var(--paper)"/>
    <path d="M0 100 C40 92 80 80 119 70" fill="none" stroke="var(--orange)" stroke-width="5"/>
  </svg>
  <div class="brand-name" style="left:0;top:44px;width:119px;justify-content:center;font-size:23px;">TAVRELO</div>
  <h2 class="headline" style="left:0;top:108px;width:119px;text-align:center;font-size:33px;line-height:1.05;">LOSE<br>15 LBS</h2>
  <p class="subline" style="left:0;top:181px;width:119px;text-align:center;font-size:16px;">in 3 months</p>
  <div class="cta block" style="left:5px;top:211px;width:110px;height:77px;font-size:17px;">TRY<br>TAVRELO<br>TODAY</div>
  <div class="bottle-photo" role="img" aria-label="Supplement bottle" style="left:12px;top:293px;width:97px;height:190px;"></div>
  <div class="model-photo green-top" role="img" aria-label="Smiling woman in green top with arms raised" style="left:18px;top:470px;width:101px;height:129px;"></div>
  <div class="natural-badge orange" style="left:6px;top:512px;width:64px;height:64px;font-size:13px;"><span class="pct">100<sup>%</sup></span><span>natural</span></div>
</section>

<!-- 728 x 90 -->
<section class="banner banner-leaderboard" style="left:258px;top:607px;width:727px;height:89px;">
  <div class="backdrop" role="img" aria-label="Soft misty backdrop"></div>
  <div class="brand-name" style="left:14px;top:46px;font-size:25px;">TAVRELO</div>
  <h2 class="headline" style="left:175px;top:17px;font-size:27px;">Lose weight</h2>
  <p class="subline" style="left:176px;top:50px;font-size:15px;">using ancient Chinese herbs</p>
  <div class="cta block" style="left:394px;top:7px;width:96px;height:76px;font-size:16px;">TRY<br>TAVRELO<br>TODAY</div>
  <div class="natural-badge" style="left:497px;top:12px;width:66px;height:66px;font-size:13px;"><span class="pct">100<sup>%</sup></span><span>natural</span></div>
  <div class="model-photo" role="img" aria-label="Slim woman in orange top with arms raised" style="left:567px;top:0;width:90px;height:89px;"></div>
  <div class="bottle-photo" role="img" aria-label="Supplement bottle" style="left:664px;top:2px;width:60px;height:87px;"></div>
</section>

</body>
</html>
```